Logo, Business Card & Stationery Design Project

Firstly, we need a quick turnaround for this project.
The company is KLT Financial.
KLT Financial specialises in sourcing, marketing and introducing clients to hassle free investment property opportunities. We are looking for a design representing stability, professionalism and customer focused. We also need to have the feel of being approachable and practical.
The design will be for the logo initially followed by business cards, letterhead (inc word based doc), with compliments, envelopes, stickers and Word documents for a letterhead & title page.
We look forward to seeing your designs.
Target Market(s)
Generally middle class couples aged from 30-50
Industry/Entity Type
Investment
Look and feel
Each slider illustrates characteristics of the customer's brand and the style your logo design should communicate.

```html
<!DOCTYPE html>
<html lang="en">
<head>
<meta charset="utf-8">
<title>KLT Financial – Identity &amp; Stationery</title>
<link rel="stylesheet" href="https://fonts.googleapis.com/css2?family=Arimo:wght@400;700&display=swap">
<style>
  :root {
    --brand-blue: #29a8e0;
    --brand-blue-deep: #1f8fc4;
    --ink: #111111;
    --paper: #ffffff;
    --paper-shade: #f3f3f3;
    --ghost: #ececec;
    --rule: #dcdcdc;
    --fine-text: #6d6d6d;
  }
  * { box-sizing: border-box; margin: 0; padding: 0; }
  html, body { width: 1200px; height: 900px; overflow: hidden; background: var(--paper); }
  body { position: relative; font-family: "Arimo", Arial, sans-serif; color: var(--ink); }

  /* wordmark */
  .wordmark { position: absolute; display: flex; align-items: flex-start; gap: 0.18em; font-weight: 400; color: var(--ink); line-height: 0.95; }
  .wordmark__square { width: 0.62em; height: 0.62em; background: var(--brand-blue); margin-top: 0.12em; flex: none; }
  .wordmark__name { display: flex; flex-direction: column; }

  .wordmark--primary { left: 76px; top: 40px; font-size: 92px; }
  .wordmark--card { left: 12px; top: 10px; font-size: 24px; }
  .wordmark--envelope { left: 22px; top: 104px; font-size: 44px; }
  .wordmark--letterhead { left: 34px; top: 34px; font-size: 44px; }

  /* business card */
  .business-card { position: absolute; left: 186px; top: 294px; width: 128px; height: 206px; background: var(--brand-blue); overflow: hidden; box-shadow: 0 0 0 1px var(--rule); }
  .business-card__head { position: relative; height: 72px; background: var(--paper); }
  .business-card__body { padding: 10px 12px; color: var(--paper); }
  .business-card__name { font-size: 17px; line-height: 1.1; }
  .business-card__role { font-size: 6px; margin-top: 2px; opacity: 0.9; }
  .business-card__contact { font-size: 5.5px; line-height: 1.5; margin-top: 14px; }
  .business-card__phones { font-size: 5.5px; line-height: 1.5; margin-top: 24px; }

  /* envelope */
  .envelope { position: absolute; left: 44px; top: 516px; width: 520px; height: 326px; background: var(--paper-shade); box-shadow: 0 0 0 1px var(--rule); overflow: hidden; }
  .envelope__flap { position: absolute; left: 0; top: 0; width: 520px; height: 90px; }
  .envelope__flap-text { position: absolute; right: 12px; top: 26px; font-size: 6.5px; color: var(--paper); letter-spacing: 0.02em; }
  .envelope__ghost { position: absolute; right: 0; top: 150px; width: 300px; height: 176px; background: var(--ghost); }

  /* letterhead */
  .letterhead { position: absolute; left: 690px; top: 176px; width: 466px; height: 678px; background: var(--paper); box-shadow: 0 0 0 1px var(--rule); overflow: hidden; }
  .letterhead__ghost { position: absolute; right: 0; top: 300px; width: 310px; height: 378px; background: var(--paper-shade); }
  .letterhead__divider { position: absolute; left: 130px; top: 560px; width: 1px; height: 112px; background: #cfe8f5; }
  .letterhead__contact { position: absolute; left: 50px; top: 580px; font-size: 6.5px; line-height: 1.55; color: var(--fine-text); }
  .letterhead__contact p + p { margin-top: 12px; }
</style>
</head>
<body>

  <div class="wordmark wordmark--primary">
    <span class="wordmark__square"></span>
    <span class="wordmark__name"><span>KLT</span><span>Financial</span></span>
  </div>

  <article class="business-card">
    <div class="business-card__head">
      <div class="wordmark wordmark--card">
        <span class="wordmark__square"></span>
        <span class="wordmark__name"><span>KLT</span><span>Financial</span></span>
      </div>
    </div>
    <div class="business-card__body">
      <p class="business-card__name">Daniel Hart</p>
      <p class="business-card__role">Account Manager</p>
      <p class="business-card__contact">d.hart@kltfinancial.com<br>www.kltfinancial.com</p>
      <p class="business-card__phones">T +44 (0)20 7946 0182<br>M +44 (0)7700 900 415</p>
    </div>
  </article>

  <article class="envelope">
    <div class="envelope__ghost"></div>
    <svg class="envelope__flap" viewBox="0 0 520 90" aria-hidden="true">
      <path d="M0 0 H520 V58 C420 70 330 66 250 62 C160 58 80 62 0 56 Z" fill="var(--brand-blue)"/>
    </svg>
    <p class="envelope__flap-text">020 7946 0182 &bull; 07700 900 415 &bull; info@kltfinancial.com &bull; www.kltfinancial.com</p>
    <div class="wordmark wordmark--envelope">
      <span class="wordmark__square"></span>
      <span class="wordmark__name"><span>KLT</span><span>Financial</span></span>
    </div>
  </article>

  <article class="letterhead">
    <div class="letterhead__ghost"></div>
    <div class="wordmark wordmark--letterhead">
      <span class="wordmark__square"></span>
      <span class="wordmark__name"><span>KLT</span><span>Financial</span></span>
    </div>
    <div class="letterhead__divider"></div>
    <div class="letterhead__contact">
      <p>100 Example Road<br>London</p>
      <p>info@kltfinancial.com<br>www.kltfinancial.com</p>
      <p>T +44 (0)20 7946 0182<br>F +44 (0)20 7946 0183</p>
    </div>
  </article>

</body>
</html>
```